Electronic Refurbishment Warehouse needs a Website

We are looking for a clean, professional looking design with iconic imagery. Our main point we want to get across is that we will help clients save time, and money, and provide outstanding quality. Our logo can be found in the uploads section. This site is used to impress clients that we have a pre-existing relationship with. This site will be available for the public but it will not be used to advertise to the public or to drive traffic to it. The color scheme we are looking to stay with is blue, but that is not to say that everything should be a shade of blue. Last note, see site map below.

Site Map:

Home
Company
a. company overview
b. CEO letter
Services
a. Remanufacture & Refurbishment Services
1. Consumer Electronics
2. Cellular Phones
b.Reverse Logistics Management
c.Warranty Repair & Field Services
d.Quality Control & Assurance
e.Warehousing & Distribution
Careers
Contact Us

Reason: We want to allocate more time for designers to do what they do best.

Target Market(s)

Phone and TV Retailers that may have units that need to be refurbished. Example Velorin, tallcart, qvo, etc.

Industry/Entity Type

Electronics

Requirements
Must have
• Home Page Slider.
Iconic imagery and navigation.
The ability to be put into the 960 Grid.

```html
<!DOCTYPE html>
<html lang="en">
<head>
<meta charset="utf-8">
<title>Korvane Group — Repair and Refurbishment Services</title>
<link href="https://fonts.googleapis.com/css2?family=Arimo:wght@400;700&display=swap" rel="stylesheet">
<style>
:root{
  --navy:#0b2a48;
  --navy-deep:#061a30;
  --hero-blue:#0a74c6;
  --hero-light:#2a9de6;
  --nav-black:#1b1b1b;
  --pill:#1a8cc2;
  --white:#ffffff;
  --cream:#f1efe4;
  --band-grey:#c9c9c4;
  --accent-blue:#1e86d4;
  --link-cyan:#4fc3f0;
  --text-dark:#0d2c4e;
  --header-top:#ffffff;
  --header-bottom:#bfc3c7;
}
*{margin:0;padding:0;box-sizing:border-box}
html,body{width:1200px;height:967px;overflow:hidden}
body{font-family:"Arimo",Arial,sans-serif;background:var(--cream);position:relative;color:var(--white)}
.abs{position:absolute}

/* header */
.site-header{left:0;top:0;width:1200px;height:84px;background:linear-gradient(var(--header-top),var(--header-bottom));border-top:5px solid var(--navy-deep)}
.brand{left:175px;top:26px;display:flex;align-items:center;gap:10px;color:var(--text-dark);font-size:24px;font-weight:700}
.brand-mark{width:34px;height:34px;background:var(--accent-blue)}
.account-links{right:170px;top:14px;font-size:12px;color:#111}
.call-box{left:835px;top:37px;width:195px;height:31px;background:var(--navy);border-radius:4px;font-size:17px;line-height:31px;text-align:center}
.headset{left:804px;top:41px}

/* nav */
.nav-band{left:0;top:84px;width:1200px;height:46px;background:linear-gradient(var(--navy-deep),#0d3a64)}
.main-nav{left:165px;top:82px;width:865px;height:62px;background:linear-gradient(#333,var(--nav-black));border-radius:0 0 6px 6px;box-shadow:0 2px 6px rgba(0,0,0,.5);z-index:3}
.nav-item{top:15px;font-size:18px;line-height:33px}
.nav-item.active{background:linear-gradient(#35a9dc,var(--pill));border-radius:6px;padding:0 12px;border:1px solid #7fd0f1}
.search-label{left:553px;top:16px;font-size:17px;line-height:33px}
.search-input{left:616px;top:19px;width:183px;height:26px;background:#555;border-radius:2px;color:#aaa;font-size:10px;line-height:26px;padding-left:36px}
.search-go{left:805px;top:19px;width:40px;height:26px;background:var(--pill);border:1px solid #7fd0f1;border-radius:3px;font-size:13px;line-height:24px;text-align:center}

/* hero */
.hero{left:0;top:130px;width:1200px;height:345px;background:radial-gradient(ellipse at 55% 30%,var(--hero-light),var(--hero-blue) 60%,#075ea5)}
.hero-title{left:229px;top:86px;font-size:24px;font-weight:700;line-height:28px}
.hero-title span{display:block;font-size:19.5px;line-height:24px}
.hero-text{left:229px;top:146px;width:405px;font-size:13px;line-height:17.5px}
.hero-cta{left:248px;top:266px;font-size:21px;font-weight:700}
.hero-arrow{left:298px;top:438px;z-index:2}
.slider-prev{left:168px;top:150px}
.slider-next{left:996px;top:150px}
.hero-visual{left:652px;top:46px;width:323px;height:268px;border-radius:14px;background:linear-gradient(135deg,#3b4856,#0e1116)}

/* welcome */
.welcome{left:0;top:475px;width:1200px;height:198px;background:linear-gradient(#0e4472,var(--navy) 70%)}
.welcome-visual{left:195px;top:24px;width:155px;height:128px;border-radius:14px;background:linear-gradient(160deg,#4a6f9a,#132a48)}
.welcome-title{left:374px;top:36px;font-size:23px}
.welcome-title b{font-weight:700}
.welcome-rule{left:374px;top:72px;width:446px;height:1px;background:#2d5f8c}
.welcome-text{left:376px;top:82px;width:445px;font-size:11.5px;line-height:15px}
.welcome-link{left:376px;top:156px;font-size:11.5px;color:var(--link-cyan)}
.quote-card{left:854px;top:30px;width:176px;height:138px;border-radius:4px;background:linear-gradient(135deg,#eef3f9,#b9cde2);color:var(--text-dark)}
.quote-card p{position:absolute;left:18px;font-weight:700}

/* services */
.grey-band{left:0;top:673px;width:1200px;height:11px;background:var(--band-grey)}
.card{top:706px;width:262px;height:151px;border:1px solid #888;overflow:hidden}
.card-title{position:absolute;font-size:19px;font-weight:700;line-height:20px}
.card-cta{position:absolute;font-size:17px;font-weight:700}

/* footer */
.footer-line{left:0;top:885px;width:1200px;height:8px;background:var(--accent-blue)}
.site-footer{left:0;top:893px;width:1200px;height:74px;background:var(--navy-deep)}
.footer-links{left:168px;top:25px;font-size:10px;color:#c8d6e6;line-height:13px}
.follow{left:865px;top:29px;font-size:15px}
.social{top:31px;width:15px;height:15px;border-radius:2px}
</style>
</head>
<body>

<header class="site-header abs">
  <div class="brand abs"><span class="brand-mark"></span>Korvane Group</div>
  <div class="account-links abs">Login &nbsp;| Register</div>
  <svg class="headset abs" width="24" height="24" viewBox="0 0 24 24" aria-hidden="true">
    <path d="M4 14v-2a8 8 0 0 1 16 0v2" fill="none" stroke="#222" stroke-width="2"/>
    <rect x="2" y="13" width="5" height="7" rx="2" fill="#222"/>
    <rect x="17" y="13" width="5" height="7" rx="2" fill="#222"/>
  </svg>
  <div class="call-box abs">Call Us: 555-014-2290</div>
</header>

<div class="nav-band abs"></div>
<nav class="main-nav abs">
  <span class="nav-item abs" style="left:28px">Home</span>
  <span class="nav-item abs" style="left:106px">Company</span>
  <span class="nav-item active abs" style="left:200px">Services</span>
  <span class="nav-item abs" style="left:309px">Careers</span>
  <span class="nav-item abs" style="left:402px">Contact Us</span>
  <span class="search-label abs">Search</span>
  <div class="search-input abs">enter your text here...</div>
  <div class="search-go abs">Go</div>
</nav>

<section class="hero abs">
  <svg class="slider-prev abs" width="34" height="40" viewBox="0 0 34 40" aria-hidden="true"><path d="M26 2 8 20l18 18" fill="none" stroke="#6fb6e6" stroke-width="8"/></svg>
  <svg class="slider-next abs" width="34" height="40" viewBox="0 0 34 40" aria-hidden="true"><path d="M8 2l18 18L8 38" fill="none" stroke="#6fb6e6" stroke-width="8"/></svg>
  <h1 class="hero-title abs">Repair and Refurbishment Services<span>for Electronics Components</span></h1>
  <p class="hero-text abs">Lorem ipsum dolor sit amet, consectetur adipiscing elit. Vivamus orci mauris, ultricies sed pellentesque eleifend, mollis vitae mauris. Nullam eu mi quis quam faucibus rutrum eu id lectus. Aliquam erat volutpat. Aenean in mattis enim. Donec sed nulla sed leo consequat fermentum nec id mauris.</p>
  <p class="hero-cta abs">Signup for your free account now!</p>
  <div class="hero-visual abs" role="img" aria-label="Three mobile phones showing a messenger contact list"></div>
</section>

<section class="welcome abs">
  <div class="welcome-visual abs" role="img" aria-label="Slide-out keyboard phone showing a photo of friends"></div>
  <h2 class="welcome-title abs" style="font-weight:400">Welcome to <b>Korvane Group</b></h2>
  <div class="welcome-rule abs"></div>
  <p class="welcome-text abs">Lorem ipsum dolor sit amet, consectetur adipiscing elit. Vivamus orci mauris, ultricies sed pellentesque eleifend, mollis vitae mauris. Nullam eu mi quis quam faucibus rutrum eu id lectus. Aliquam erat volutpat. Aenean in mattis enim. Donec sed nulla sed leo consequat fermentum nec id mauris.</p>
  <p class="welcome-link abs">&#9656;&nbsp; Click here for more information...</p>
  <div class="quote-card abs" role="img" aria-label="Request a quote card with a world map and a computer mouse">
    <p style="top:34px;font-size:21px;line-height:22px">Request<br>A free Quote</p>
    <p style="top:82px;font-size:16px">Click here</p>
  </div>
</section>

<svg class="hero-arrow abs" width="220" height="52" viewBox="0 0 220 52" aria-hidden="true">
  <path d="M0 0h220L110 44z" fill="#ffffff"/>
  <path d="M70 28 110 44 150 28 150 36 110 52 70 36z" fill="#1a7fd0"/>
</svg>

<div class="grey-band abs"></div>

<a class="card abs" style="left:166px;background:linear-gradient(135deg,#a9c6e8,#2f6fb8)" role="img" aria-label="Mobile phone with headphones">
  <span class="card-title" style="left:114px;top:48px;font-size:16px;line-height:18px">Remanufacture &amp;<br>Refurbishment<br><span style="font-size:20px">Services</span></span>
  <span class="card-cta" style="left:132px;top:116px">Click here</span>
</a>
<a class="card abs" style="left:467px;background:linear-gradient(135deg,#8a8f94,#3a3f44)" role="img" aria-label="Warehouse worker standing among storage shelves">
  <span class="card-title" style="left:9px;top:104px;font-size:21px">Career Opportunities</span>
  <span class="card-cta" style="left:11px;top:127px;font-size:12px">Our employees are the key to our success</span>
</a>
<a class="card abs" style="left:768px;background:linear-gradient(#6f8696,#2c4658)" role="img" aria-label="Cargo ship at sea">
  <span class="card-title" style="left:16px;top:60px;font-size:20px;line-height:22px">Reverse Logistics<br><span style="font-size:24px">Management</span></span>
  <span class="card-cta" style="left:18px;top:116px">Click here</span>
</a>

<div class="footer-line abs"></div>
<footer class="site-footer abs">
  <p class="footer-links abs">Home &nbsp;-- &nbsp;Company &nbsp;-- &nbsp;Services &nbsp;-- &nbsp;Careers &nbsp;-- &nbsp;Contact Us<br>Copyright©2012 Korvane Group . Privacy Policy.</p>
  <span class="follow abs">Follow Us On:</span>
  <span class="social abs" style="left:970px;background:#3b5b9a"></span>
  <span class="social abs" style="left:992px;background:#35a8e0"></span>
  <span class="social abs" style="left:1015px;background:#c9302c"></span>
</footer>

</body>
</html>
```